Course Graduation Certificate

This project is not for a flyer but instead for the creation of a course graduation certificate. The final certificate needs to include the Marlowe Summit Aviation Academy logo and the text stating as follows:
Certifies that ___________________________ has satisfactorily completed the course of _______________________________ on ________________________________
I would also like to include some type of gold seal of completion as well as a place to sign my name and credentials at the bottom of the certificate
I have included the Marlowe Summit Aviation Academy logo as well as three other certificate examples for you to work from.
Target Market(s)
Students completing a certification course and receiving a certificate
Look and feel

```html
<!DOCTYPE html>
<html lang="en">
<head>
<meta charset="utf-8">
<title>Course Graduation Certificate</title>
<link rel="stylesheet" href="https://fonts.googleapis.com/css2?family=UnifrakturMaguntia&family=Domine:wght@500;600&family=Libre+Baskerville:wght@400;700&display=swap">
<style>
  :root {
    --backdrop: #808080;
    --paper: #e6e6e6;
    --cobalt: #0b50b3;
    --name-blue: #1577c0;
    --ink: #3a3a3a;
    --ink-soft: #2b2b2b;
    --gold-light: #f3d27a;
    --gold: #d4a437;
    --gold-deep: #a87a1c;
  }
  * { box-sizing: border-box; margin: 0; padding: 0; }
  html, body {
    width: 845px; height: 1200px; overflow: hidden;
    background: var(--backdrop);
  }
  .certificate {
    position: absolute; left: 22px; top: 317px;
    width: 800px; height: 566px;
    background: var(--paper);
    font-family: "Libre Baskerville", Georgia, serif;
    color: var(--ink-soft);
  }
  .frame { position: absolute; inset: 0; width: 800px; height: 566px; }
  .corner-ornament {
    position: absolute; width: 83px; height: 83px;
    background: var(--cobalt); opacity: .92;
    border-radius: 4px 40px 4px 40px;
  }
  .corner-ornament.top-left { left: 22px; top: 18px; }
  .corner-ornament.top-right { right: 22px; top: 18px; border-radius: 40px 4px 40px 4px; }
  .corner-ornament.bottom-left { left: 22px; bottom: 18px; border-radius: 40px 4px 40px 4px; }
  .corner-ornament.bottom-right { right: 22px; bottom: 18px; }

  .academy-name {
    position: absolute; left: 0; right: 0; top: 28px;
    text-align: center;
    font-family: "Domine", Georgia, serif; font-weight: 600;
    font-size: 11px; line-height: 12px; letter-spacing: 2px;
    color: var(--cobalt);
  }

  .title {
    position: absolute; left: 0; right: 0; top: 50px;
    text-align: center;
    font-family: "UnifrakturMaguntia", "Old English Text MT", serif;
    font-weight: 400; font-size: 136px; line-height: 1;
    color: var(--cobalt);
  }
  .subtitle {
    position: absolute; left: 0; right: 0; top: 190px;
    display: flex; justify-content: center; align-items: center; gap: 6px;
    font-family: "Domine", Georgia, serif; font-weight: 500;
    font-size: 22px; line-height: 26px; color: var(--ink);
  }
  .subtitle .dash { width: 26px; height: 2px; background: var(--cobalt); position: relative; }
  .subtitle .dash::after {
    content: ""; position: absolute; top: -2px; width: 5px; height: 5px;
    background: var(--cobalt); transform: rotate(45deg);
  }
  .subtitle .dash.left::after { left: 6px; }
  .subtitle .dash.right::after { right: 6px; }

  .recipient {
    position: absolute; left: 0; right: 0; top: 256px;
    text-align: center;
    font-family: "Libre Baskerville", Georgia, serif; font-weight: 700;
    font-size: 36px; line-height: 42px; color: var(--name-blue);
  }
  .statement {
    position: absolute; left: 0; right: 0;
    text-align: center; font-size: 8.5px; line-height: 12px; color: var(--ink-soft);
    white-space: nowrap;
  }
  .statement.main { top: 322px; }
  .statement.on { top: 346px; }

  .sign-block {
    position: absolute; top: 436px; width: 136px; text-align: center;
  }
  .sign-block .rule {
    height: 2px; background: linear-gradient(90deg, transparent, var(--cobalt) 30%, var(--cobalt) 70%, transparent);
  }
  .sign-block .label {
    margin-top: 7px; font-family: "Domine", Georgia, serif; font-weight: 600;
    font-size: 11px; letter-spacing: 3px; color: var(--ink);
  }
  .sign-block.date { left: 135px; }
  .sign-block.signature { left: 530px; }
  .signature-mark {
    position: absolute; left: 544px; top: 392px; width: 96px; height: 36px;
    background: linear-gradient(90deg, #3a3a3a33, #1a1a1a55, #3a3a3a33);
    border-radius: 18px;
  }
  .completion-seal {
    position: absolute; left: 350px; top: 392px; width: 100px; height: 100px;
    border-radius: 50%;
    background: radial-gradient(circle at 40% 35%, var(--gold-light) 0%, var(--gold) 55%, var(--gold-deep) 100%);
  }
</style>
</head>
<body>
  <main class="certificate">
    <svg class="frame" viewBox="0 0 800 566" aria-hidden="true">
      <g stroke="#0b50b3" fill="#0b50b3">
        <line x1="111" y1="34" x2="209" y2="34" stroke-width="2"/>
        <line x1="591" y1="34" x2="689" y2="34" stroke-width="2"/>
        <line x1="222" y1="34" x2="260" y2="34" stroke-width="2" stroke-dasharray="1.5 5" stroke-linecap="round"/>
        <line x1="542" y1="34" x2="580" y2="34" stroke-width="2" stroke-dasharray="1.5 5" stroke-linecap="round"/>
        <circle cx="160" cy="34" r="5" stroke="none"/>
        <circle cx="640" cy="34" r="5" stroke="none"/>
        <line x1="111" y1="534" x2="209" y2="534" stroke-width="2"/>
        <line x1="591" y1="534" x2="689" y2="534" stroke-width="2"/>
        <line x1="220" y1="534" x2="580" y2="534" stroke-width="2" stroke-dasharray="1.5 5" stroke-linecap="round"/>
        <circle cx="160" cy="534" r="5" stroke="none"/>
        <circle cx="640" cy="534" r="5" stroke="none"/>
        <line x1="34" y1="110" x2="34" y2="456" stroke-width="2"/>
        <line x1="766" y1="110" x2="766" y2="456" stroke-width="2"/>
        <circle cx="34" cy="159" r="5" stroke="none"/>
        <circle cx="34" cy="410" r="5" stroke="none"/>
        <circle cx="766" cy="159" r="5" stroke="none"/>
        <circle cx="766" cy="410" r="5" stroke="none"/>
      </g>
    </svg>

    <div class="corner-ornament top-left" role="img" aria-label="Blue scrollwork corner ornament"></div>
    <div class="corner-ornament top-right" role="img" aria-label="Blue scrollwork corner ornament"></div>
    <div class="corner-ornament bottom-left" role="img" aria-label="Blue scrollwork corner ornament"></div>
    <div class="corner-ornament bottom-right" role="img" aria-label="Blue scrollwork corner ornament"></div>

    <p class="academy-name">MARLOWE SUMMIT AVIATION ACADEMY</p>

    <h1 class="title">Certificate</h1>
    <p class="subtitle"><span class="dash left"></span>Course Graduation<span class="dash right"></span></p>

    <p class="recipient">ELENA MARSH</p>

    <p class="statement main">Certifies that ___________________________ has satisfactorily completed the course of _______________________________</p>
    <p class="statement on">on ________________________________</p>

    <div class="completion-seal" role="img" aria-label="Gold seal of completion"></div>

    <div class="sign-block date">
      <div class="rule"></div>
      <p class="label">DATE</p>
    </div>

    <div class="signature-mark" role="img" aria-label="Handwritten signature"></div>
    <div class="sign-block signature">
      <div class="rule"></div>
      <p class="label">SIGNATURE</p>
    </div>
  </main>
</body>
</html>
```